Postcard design to acquire new clients for my Property Management Company

I'm looking for a postcard design that I can send to prospective clients detailing information about my company and services.
Postcard should be eye catching and contain information from www.brightkeyrentals-example.com. I've provided a few screen shots for the most important information and my logo.
Target Market(s)
Real Estate
Industry/Entity Type
Real Estate
Font styles to use
Sans Serif
Requirements
Must have
- Must be eye catching!! this will be a direct mail piece - I'd like for the card to be read and not tossed in the trash immediately.
Design que from the logo.
A place to write / print the receipts name and address.
our physical address - 2287 Marble Lane, Lubbock, TX 79555.
Should not have
- the contact information on the business card is not accurate - please use info from website.

```html
<!DOCTYPE html>
<html lang="en">
<head>
<meta charset="utf-8">
<title>BrightKey Property Management – Postcard</title>
<link rel="stylesheet" href="https://fonts.googleapis.com/css2?family=Montserrat:wght@400;500;600;800&display=swap">
<style>
  :root {
    --backdrop: #2a2726;
    --brand-blue: #0d4a7d;
    --band-blue: #0b4c80;
    --charcoal: #3d3d3d;
    --charcoal-dark: #262626;
    --white: #ffffff;
    --ink: #1d1d1d;
    --rule: #9a9a9a;
    --sky-top: #d9e2ee;
    --sky-mid: #aebdd0;
    --lawn: #5d8a3a;
    --dusk-top: #55606f;
    --dusk-mid: #3d4552;
    --street: #6e4a3a;
  }
  * { box-sizing: border-box; margin: 0; padding: 0; }
  html, body {
    width: 1024px; height: 1200px; overflow: hidden;
    background: var(--backdrop);
    font-family: "Montserrat", Arial, sans-serif;
  }
  .stage {
    position: relative; width: 1000px; height: 1172px;
    transform: scale(1.024); transform-origin: 0 0;
  }
  .postcard {
    position: absolute; left: 98px; width: 803px; height: 443px;
    background: var(--white); overflow: hidden;
    box-shadow: 0 6px 18px rgba(0,0,0,.45);
  }
  .postcard--front { top: 84px; }
  .postcard--back { top: 607px; }
  .postcard__shapes { position: absolute; inset: 0; width: 803px; height: 443px; }
  .headline {
    position: absolute; left: 44px; top: 34px;
    font-weight: 800; font-size: 37px; line-height: 40px; letter-spacing: .3px;
    text-transform: uppercase; color: var(--brand-blue);
  }
  .headline--light { color: var(--white); }
  .brand-name {
    position: absolute; left: 560px; top: 34px; width: 208px; text-align: right;
    font-weight: 600; font-size: 19px; line-height: 20px; letter-spacing: 2px;
    color: var(--brand-blue); text-transform: uppercase;
  }
  .brand-name small { display: block; font-size: 9.5px; line-height: 12px; letter-spacing: 1.4px; }
  .plan {
    position: absolute; top: 207px; width: 108px; height: 107px;
    background: var(--white); border-radius: 5px;
    box-shadow: 0 2px 7px rgba(0,0,0,.22);
    text-align: center; color: var(--ink);
  }
  .plan__name { margin-top: 13px; font-size: 15px; }
  .plan__rate { margin-top: 6px; font-weight: 800; font-size: 31px; color: var(--brand-blue); }
  .plan__basis { margin-top: 6px; font-size: 9px; }
  .cta { position: absolute; left: 45px; color: var(--white); }
  .cta__title { font-weight: 500; font-size: 22px; letter-spacing: 1.3px; line-height: 26px; }
  .cta__email { display: flex; align-items: center; gap: 7px; font-size: 15px; letter-spacing: .8px; margin-top: 1px; }
  .contact { position: absolute; color: var(--white); text-align: center; width: 330px; }
  .contact__phone { display: flex; align-items: center; justify-content: center; gap: 10px; font-size: 28px; letter-spacing: 1px; }
  .contact__web { margin-top: 8px; font-size: 14px; letter-spacing: .8px; }
  .services {
    position: absolute; left: 45px; top: 140px;
    display: grid; grid-template-columns: 198px 200px; row-gap: 25px;
    list-style: none; color: var(--white); font-size: 15px;
  }
  .services li { display: flex; align-items: center; gap: 9px; height: 20px; }
  .stamp-box { position: absolute; left: 674px; top: 39px; width: 88px; height: 88px; border: 1.5px solid var(--rule); }
  .address-line { position: absolute; left: 498px; width: 263px; height: 0; border-top: 1px solid var(--rule); }
</style>
</head>
<body>
<main class="stage">

  <!-- Front -->
  <section class="postcard postcard--front">
    <svg class="postcard__shapes" viewBox="0 0 803 443" aria-hidden="true">
      <defs>
        <linearGradient id="houseScene" x1="0" y1="0" x2="0" y2="1">
          <stop offset="0" stop-color="var(--sky-top)"/>
          <stop offset=".45" stop-color="var(--sky-mid)"/>
          <stop offset=".62" stop-color="#7a5a4c"/>
          <stop offset=".78" stop-color="var(--lawn)"/>
          <stop offset="1" stop-color="#4e7a30"/>
        </linearGradient>
      </defs>
      <polygon points="395,0 412,0 552,443 517,443" fill="var(--band-blue)"/>
      <polygon points="412,0 803,0 803,443 552,443" fill="url(#houseScene)" role="img" aria-label="Photo of a large brick family house with a green lawn"/>
      <rect x="0" y="335" width="430" height="64" fill="var(--band-blue)"/>
      <polygon points="416,320 803,320 803,426 392,426" fill="var(--charcoal-dark)"/>
      <polygon points="429,317 803,317 803,423 400,423" fill="var(--charcoal)"/>
    </svg>

    <h1 class="headline">Choose the<br>right property<br>management<br>system</h1>
    <div class="brand-name">BrightKey<small>Property Management</small></div>

    <div class="plan" style="left:44px"><p class="plan__name">Lease Only</p><p class="plan__rate">9%</p><p class="plan__basis">of annual lease</p></div>
    <div class="plan" style="left:167px"><p class="plan__name">Full Service</p><p class="plan__rate">10%</p><p class="plan__basis">of monthly rent</p></div>
    <div class="plan" style="left:290px"><p class="plan__name">Premium</p><p class="plan__rate">12%</p><p class="plan__basis">of monthly rent</p></div>

    <div class="cta" style="top:343px">
      <p class="cta__title">CALL FOR FREE QUOTE</p>
      <p class="cta__email"><svg width="13" height="10" viewBox="0 0 13 10"><rect x=".6" y=".6" width="11.8" height="8.8" fill="none" stroke="#fff" stroke-width="1.2"/><path d="M.6 .6 6.5 5.5 12.4 .6" fill="none" stroke="#fff" stroke-width="1.2"/></svg>info@brightkeyrentals-example.com</p>
    </div>

    <div class="contact" style="left:460px; top:336px">
      <p class="contact__phone"><svg width="34" height="34" viewBox="0 0 34 34"><circle cx="17" cy="17" r="15" fill="none" stroke="#fff" stroke-width="2.4"/><path d="M11.5 9.5c1-.9 2-.8 2.6.1l1.6 2.6c.5.8.3 1.6-.4 2.2l-1 .8c.8 2 2.4 3.8 4.4 4.8l.9-1c.6-.7 1.5-.8 2.2-.3l2.6 1.6c.8.6.9 1.7 0 2.6-1.5 1.5-3.3 1.9-5.4.9-3.6-1.7-6.6-4.8-8.2-8.5-.9-2.1-.4-4.2.7-5.8z" fill="#fff"/></svg>(806) 555-0142</p>
      <p class="contact__web">www.brightkeyrentals-example.com</p>
    </div>
  </section>

  <!-- Back -->
  <section class="postcard postcard--back">
    <svg class="postcard__shapes" viewBox="0 0 803 443" aria-hidden="true">
      <defs>
        <linearGradient id="cityScene" x1="0" y1="0" x2="0" y2="1">
          <stop offset="0" stop-color="var(--dusk-top)"/>
          <stop offset=".55" stop-color="var(--dusk-mid)"/>
          <stop offset=".8" stop-color="#3a2f2e"/>
          <stop offset="1" stop-color="var(--street)"/>
        </linearGradient>
      </defs>
      <polygon points="0,0 389,0 507,443 0,443" fill="url(#cityScene)" role="img" aria-label="Photo of a downtown street at dusk with office buildings"/>
      <polygon points="389,0 405,0 542,443 507,443" fill="var(--band-blue)"/>
      <rect x="0" y="336" width="430" height="63" fill="var(--band-blue)"/>
      <polygon points="412,321 803,321 803,425 392,425" fill="var(--charcoal-dark)"/>
      <polygon points="424,318 803,318 803,422 400,422" fill="var(--charcoal)"/>
    </svg>

    <h2 class="headline headline--light">Discover our<br>services</h2>

    <ul class="services">
      <li><span>✓</span>Property Marketing</li>
      <li><span>✓</span>Tenant Screening</li>
      <li><span>✓</span>Rent Collection</li>
      <li><span>✓</span>Maintenance</li>
      <li><span>✓</span>Property Inspections</li>
      <li><span>✓</span>Financial Reporting</li>
      <li><span>✓</span>Evictions</li>
      <li><span>✓</span>Legal Guidance</li>
    </ul>

    <div class="stamp-box"></div>
    <div class="address-line" style="top:186px"></div>
    <div class="address-line" style="top:223px"></div>
    <div class="address-line" style="top:260px"></div>

    <div class="cta" style="top:344px">
      <p class="cta__title">CALL FOR FREE QUOTE</p>
      <p class="cta__email"><svg width="13" height="10" viewBox="0 0 13 10"><rect x=".6" y=".6" width="11.8" height="8.8" fill="none" stroke="#fff" stroke-width="1.2"/><path d="M.6 .6 6.5 5.5 12.4 .6" fill="none" stroke="#fff" stroke-width="1.2"/></svg>info@brightkeyrentals-example.com</p>
    </div>

    <div class="contact" style="left:438px; top:337px">
      <p class="contact__phone"><svg width="34" height="34" viewBox="0 0 34 34"><circle cx="17" cy="17" r="15" fill="none" stroke="#fff" stroke-width="2.4"/><path d="M11.5 9.5c1-.9 2-.8 2.6.1l1.6 2.6c.5.8.3 1.6-.4 2.2l-1 .8c.8 2 2.4 3.8 4.4 4.8l.9-1c.6-.7 1.5-.8 2.2-.3l2.6 1.6c.8.6.9 1.7 0 2.6-1.5 1.5-3.3 1.9-5.4.9-3.6-1.7-6.6-4.8-8.2-8.5-.9-2.1-.4-4.2.7-5.8z" fill="#fff"/></svg>(806) 555-0142</p>
      <p class="contact__web">www.brightkeyrentals-example.com</p>
    </div>
  </section>

</main>
</body>
</html>
```